Melbourne Gym Celebrating 49 years of business

We are celebrating our 49th birthday and will be running a "12 month Membership Special" $299.00 save over 30%. Being one of the longest running gyms in the fitness industry the design must be very eye catching and professional in its appearance. Given the length of operation, artwork must also have a touch of class that will appeal to 18-40 year old's. Below are previous specials with its layout and sample 49th Anniversary layouts. The final design should emphasis the advertised sale, along with celebrating 49 years. You can be as creative as possible with layout and design.

Target Market(s)

Male and females aged between 18-40

Font styles to use
Serif
Sans Serif

Requirements
Must have
• Must emphasize either "Celebrating 49 years" "49th Anniversary" or Happy 49th Birthday" and in a large font "12 Month Special $299.00 SAVE OVER 30%" Terms and Conditions Apply, Strictly Limited Time Only.
• "contact details"
• Address: 14 Harlow Rd Tindale Park
• Ph: 9517 2860
• www.corvalfitness.com.au
• Design format must come in poster size A0 size, Instagram format, Facebook cover and 800 x 800 for the website
Nice to have
• Given the number of years in business, an elegant/classy feel would be nice to the overall presentation. Bright colors can be used along with artistic graphic designs

```html
<!DOCTYPE html>
<html lang="en">
<head>
<meta charset="utf-8">
<title>Corval Fitness – 49 Years Anniversary Flyer</title>
<link href="https://fonts.googleapis.com/css2?family=Oswald:wght@400;500;600;700&family=Cinzel:wght@700&display=swap" rel="stylesheet">
<style>
  :root {
    --stage: #e9e9ea;
    --night-1: #0e1220;
    --night-2: #252b3d;
    --night-3: #3a4057;
    --gold-light: #ffe08a;
    --gold: #e8b53a;
    --gold-deep: #a8731a;
    --ink-dark: #2a1a05;
    --white: #ffffff;
    --muted: #c9ccd6;
    --disc: #2b2d33;
    --disc-edge: #55575e;
    --skin-1: #7a5a4a;
    --skin-2: #241d22;
  }
  * { margin: 0; padding: 0; box-sizing: border-box; }
  html, body { width: 1200px; height: 800px; overflow: hidden; background: var(--stage); }
  .canvas { position: relative; width: 1200px; height: 800px; display: flex; align-items: center; justify-content: center; }

  .flyer {
    position: relative; width: 560px; height: 764px; overflow: hidden;
    background: radial-gradient(ellipse at 40% 45%, var(--night-3) 0%, var(--night-2) 40%, var(--night-1) 100%);
    box-shadow: 0 10px 30px rgba(0,0,0,.35);
    font-family: "Oswald", "Arial Narrow", sans-serif; color: var(--white);
  }

  .athlete-photo {
    position: absolute; left: 330px; top: 140px; width: 210px; height: 560px;
    background: radial-gradient(ellipse at 50% 35%, var(--skin-1) 0%, var(--skin-2) 55%, transparent 78%);
    opacity: .9;
  }

  .badge { position: absolute; left: 50px; top: 50px; width: 320px; height: 320px; }
  .badge svg { position: absolute; inset: 0; }
  .badge-years-number {
    position: absolute; left: 0; width: 320px; top: 62px; text-align: center;
    font-family: "Cinzel", serif; font-weight: 700; font-size: 124px; line-height: 1;
    color: var(--gold); letter-spacing: -4px;
    text-shadow: 0 2px 0 var(--gold-deep), 0 0 18px rgba(255,200,80,.45);
  }
  .badge-years-label {
    position: absolute; left: 0; width: 320px; top: 200px; text-align: center;
    font-weight: 600; font-size: 26px; line-height: 1; color: var(--gold); letter-spacing: 1px;
  }
  .badge-ribbon-text {
    position: absolute; left: 0; width: 320px; top: 248px; text-align: center;
    font-family: "Cinzel", serif; font-weight: 700; font-size: 27px; line-height: 1; color: var(--ink-dark);
    transform: rotate(-4deg);
  }

  .offer-title {
    position: absolute; left: 78px; top: 400px; font-size: 38px; font-weight: 500; line-height: 1;
    letter-spacing: -.5px; transform: rotate(-3deg); transform-origin: left;
  }
  .offer-price {
    position: absolute; left: 80px; top: 458px; width: 232px; height: 54px;
    border: 2px solid var(--gold); display: flex; align-items: center; justify-content: center;
    font-size: 38px; font-weight: 600; color: var(--gold);
    transform: rotate(-3deg);
  }

  .saving-disc {
    position: absolute; left: 82px; top: 528px; width: 190px; height: 190px; border-radius: 50%;
    background: var(--disc); border: 3px solid var(--disc-edge);
    display: flex; flex-direction: column; align-items: center; justify-content: center;
  }
  .saving-disc .lead { font-size: 32px; font-weight: 600; line-height: 1; }
  .saving-disc .figure { font-size: 82px; font-weight: 600; line-height: 1; margin-top: 4px; }
  .saving-disc .figure small { font-size: 54px; }

  .brand {
    position: absolute; left: 300px; top: 650px; display: flex; align-items: center; gap: 6px;
    font-size: 22px; font-weight: 700; line-height: 1; letter-spacing: 1px;
  }
  .brand .mark { width: 10px; height: 10px; background: var(--white); }

  .terms {
    position: absolute; left: 300px; top: 680px; font-size: 10px; font-weight: 400;
    letter-spacing: .5px; color: var(--muted);
  }

  .contact {
    position: absolute; left: 0; right: 0; bottom: 22px; padding: 0 28px;
    display: flex; justify-content: space-between; font-size: 12px; font-weight: 500; letter-spacing: .3px;
  }
</style>
</head>
<body>
<main class="canvas">
  <article class="flyer">
    <div class="athlete-photo" role="img" aria-label="Photo of a female athlete holding dumbbells, seen from behind looking over her shoulder"></div>

    <section class="badge" aria-label="49 years anniversary">
      <svg viewBox="0 0 320 320" width="320" height="320" aria-hidden="true">
        <defs>
          <linearGradient id="goldSheen" x1="0" y1="0" x2="1" y2="1">
            <stop offset="0" stop-color="#ffe08a"/>
            <stop offset=".5" stop-color="#e8b53a"/>
            <stop offset="1" stop-color="#a8731a"/>
          </linearGradient>
        </defs>
        <circle cx="160" cy="145" r="122" fill="none" stroke="url(#goldSheen)" stroke-width="8"/>
        <line x1="88" y1="213" x2="118" y2="213" stroke="#e8b53a" stroke-width="2"/>
        <line x1="202" y1="213" x2="232" y2="213" stroke="#e8b53a" stroke-width="2"/>
        <rect x="20" y="240" width="280" height="40" fill="url(#goldSheen)" transform="rotate(-4 160 260)"/>
      </svg>
      <div class="badge-years-number">49</div>
      <div class="badge-years-label">YEARS</div>
      <div class="badge-ribbon-text">ANNIVERSARY</div>
    </section>

    <h2 class="offer-title">12 MONTH SPECIAL</h2>
    <div class="offer-price">$299.00</div>

    <div class="saving-disc">
      <span class="lead">SAVE OVER</span>
      <span class="figure">30<small>%</small></span>
    </div>

    <div class="brand"><span class="mark"></span>CORVAL FITNESS</div>
    <p class="terms">Terms and Conditions Apply. Strictly Limited Time Only.</p>

    <footer class="contact">
      <span>ADDRESS: 14 HARLOW RD TINDALE PARK</span>
      <span>PH: 9517 2860</span>
      <span>WWW.CORVALFITNESS.COM.AU</span>
    </footer>
  </article>
</main>
</body>
</html>
```